Power Point Template Kalmora sustainability consulting

Please note:
We are not looking for new design proposals anymore since we've already received templetes from two designers that we really like. We are currently discussing possible changes with them and will make a final decision soon. Thank you very much.

(find english description below)
We are a small German start-up that offers sustainability consulting. For presentations of results, our company presentation, proposals, lectures, etc., we need a PowerPoint template that matches our logo. We come from classic management consulting / strategy consulting and also deal with facts and figures in sustainability consulting. Therefore, the template should not be too fancy and should not only consist of photos. But it shouldn't be a completely sober template either. Our logo with the green leaves for sustainability (three leaves for KALmora) and the white bar chart (with the dynamic swing upwards) reflects our attitude well, where we see ourselves on the range from playful to sober and classic to modern.

It might be nice for the template to include the shape of one of the leaves (from the logo). Also, the logo should appear in a corner of each slide. The colors from the logo (see appendix) should be partially reflected in the presentation. We can also imagine a gold-brown tone (see website www.kalmora-consulting.example) or a coral tone as a contrast. (Attention - the website is not final yet).

For a first suggestion, it is sufficient to suggest three to four slides (cover sheet, chapter/separation slide, text slide, data slide). We will then mark drafts that we like. In total, we would then need about 6-10 more slide templates, e.g. about us, team, slide for a statement, 2-3 data charts (pie, bar, column), top 3 - 5 list, timeline, contact (more slides are welcome ).

We are a small German start-up offering sustainability consulting. We need a power point template for result presentations, our company presentation, proposals, lectures etc. The template should be aligned with our logo. Our background lies in classic management consulting / strategy consulting and we also deal with facts and figures in sustainability consulting. Therefore, the template should not be too playful and not only consist of photos. But it should also not be a completely clear template. Our logo with the green leaves for sustainability (three leaves for KALmora) and the white bar chart (with the dynamic upward swing) reflects our attitude well, where we see ourselves on the range from playful to down-to-earth and classic to modern .

For the template, it might be nice to incorporate the shape of one of the leaves (from the logo). Also, the logo should show up in one corner on each slide. Some of the colors from the logo (see attachment) should be reflected in the presentation. We could also think of a gold-brown tone (see website www.kalmora-consulting.example) or a coral tone for contrast. (Attention - the website is not final yet).

For a first proposal it is quite sufficient to suggest us three to four slides (cover page, chapter/separation slide, text slide, data slide). We will then mark the drafts that we like. In total we would need about 6-10 more slide templates, eg About us, Team, slide for a statement, 2-3 data charts (pie, bar, column), Top 3 - 5 List, Timeline, Contact (more slides are welcome).

Target Market(s)

Corporations, large companies and SMEs

Industry/Entity Type

Unternehmensberatung, Nachhaltigkeitsberatung

Font styles to use
Sans Serif
Other font styles liked:
• Calibri

Colors
00AB8E
00BBA5
67D7C9
C6EFE9
E9F9F6

Requirements
Must have
• see description (e.g. the colors of our logo)
Nice to have
• see description (e.g. elements of the logo included)
Should not have
• see description

```html
<!DOCTYPE html>
<html lang="en">
<head>
<meta charset="utf-8">
<title>Kalmora Consulting – Presentation Template</title>
<link href="https://fonts.googleapis.com/css2?family=Ubuntu:wght@300;400;500&family=Open+Sans:wght@400;600&display=swap" rel="stylesheet">
<style>
:root{
  --green-dark:#3f7a17;
  --green:#5e9a22;
  --green-light:#b3d36a;
  --green-pale:#dcebb8;
  --gray:#5f6569;
  --gray-light:#dedede;
  --text:#6a6a6a;
  --canvas:#c9c9c9;
}
*{box-sizing:border-box;margin:0;padding:0}
html,body{width:1200px;height:2786px;overflow:hidden}
body{background:var(--canvas);font-family:"Open Sans",sans-serif;color:var(--text);position:relative}
.stage{position:absolute;left:0;top:0;width:1200px;height:740px;background:linear-gradient(180deg,#e4e6ea 0%,#d6d9de 70%,#cfcfcf 100%)}
.stage-logo{position:absolute;right:48px;top:86px;text-align:right;font-family:"Ubuntu",sans-serif;font-weight:300;font-size:34px;color:var(--gray);line-height:1}
.stage-logo small{display:block;font-size:10px;color:var(--green);letter-spacing:.5px;margin-top:2px;padding-right:40px}
.stage-slide{position:absolute;left:190px;top:150px;transform:scale(1.14);transform-origin:0 0;box-shadow:0 10px 30px rgba(0,0,0,.18)}

.slide{position:absolute;width:562px;height:315px;background:linear-gradient(90deg,#fff 45%,#f2f2f2 100%);overflow:hidden;font-size:6.4px;line-height:1.3}
.slide-title{position:absolute;left:27px;top:23px;font-family:"Ubuntu",sans-serif;font-weight:300;font-size:21px;color:var(--green-dark)}
.slide-title b{font-weight:500}
.title-tab{position:absolute;left:0;top:22px;width:12px;height:26px;background:linear-gradient(180deg,var(--green-light),var(--green));border-radius:0 3px 3px 0}
.foot-logo{position:absolute;left:12px;top:276px;font-family:"Ubuntu",sans-serif;font-weight:300;font-size:12px;color:var(--gray);line-height:1}
.foot-logo small{display:block;font-size:3.5px;color:var(--green);padding-left:16px;letter-spacing:.3px}
.foot-bar{position:absolute;left:75px;right:16px;top:287px;height:8px;border-radius:4px;background:linear-gradient(90deg,var(--green-dark),var(--green) 50%,var(--green-light))}
.foot-bar span{position:absolute;right:24px;top:0;font-size:4px;line-height:8px;color:#fff}
.foot-bar i{position:absolute;right:-2px;top:-2px;width:12px;height:12px;border-radius:50%;background:var(--green-dark);color:#fff;font-style:normal;font-size:5px;line-height:12px;text-align:center}

.photo-bg{position:absolute;inset:0;background:
  radial-gradient(ellipse at 78% 55%,#6f9f2a 0%,#8dbb3b 18%,rgba(185,214,110,.7) 38%,rgba(235,240,220,0) 62%),
  radial-gradient(ellipse at 90% 5%,#f3e7b3 0%,rgba(243,231,179,0) 40%),
  linear-gradient(90deg,#f7f8f2 0%,#eef2e2 55%,#dfe9c3 100%)}
.cover-logo{position:absolute;left:45px;top:48px;font-family:"Ubuntu",sans-serif;font-weight:300;font-size:22px;color:var(--gray);line-height:1}
.cover-logo::before{content:"";display:inline-block;width:12px;height:12px;border-radius:50%;background:var(--green);margin-right:6px;vertical-align:1px}
.cover-logo small{display:block;font-size:5px;color:var(--green);padding-left:90px}
.cover-title{position:absolute;left:45px;top:116px;font-family:"Ubuntu",sans-serif;font-weight:500;font-size:28px;line-height:1.12;color:var(--green-dark)}
.cover-sub{position:absolute;left:45px;top:190px;font-size:11px;color:var(--gray);font-family:"Ubuntu",sans-serif;font-weight:300}
.url-pill{position:absolute;left:47px;top:233px;background:var(--green-dark);color:#fff;border-radius:8px;padding:3px 14px;font-size:5px}
.cover-copy{position:absolute;left:0;right:0;bottom:6px;text-align:center;font-size:4px;letter-spacing:1px;color:var(--gray)}

.body-text{position:absolute;left:41px;top:94px;width:480px;color:var(--text)}
.body-text p{margin-bottom:6px}

.team-band{position:absolute;left:0;top:0;width:100%;height:70px;background:linear-gradient(90deg,var(--green-dark),var(--green) 60%,#c0d98a)}
.team-band + .slide-title{color:#fff}
.member{position:absolute;top:68px;width:140px;text-align:center}
.member .portrait{display:block;width:106px;height:106px;margin:0 auto 6px;background:linear-gradient(180deg,#d7d9dc,#9a9ea3);border:2px solid #fff}
.member h3{font-size:9.5px;font-weight:600;color:var(--green-dark);font-family:"Open Sans",sans-serif}
.member .role{font-size:5px;color:var(--gray);margin-bottom:6px}

.col{position:absolute;top:92px;width:210px}
.col h3{font-family:"Ubuntu",sans-serif;font-weight:400;font-size:11px;color:var(--green-dark);margin-bottom:6px}
.col ul{padding-left:8px}
.col li{margin-bottom:6px}
.col li::marker{color:var(--green)}

.box{position:absolute;top:86px;width:138px;height:164px;color:#fff;text-align:center;padding:12px 10px}
.box h3{font-family:"Ubuntu",sans-serif;font-weight:400;font-size:12px;line-height:1.2;margin-bottom:14px}
.box p{font-size:5.6px;line-height:1.35}

.tl{position:absolute;top:92px;width:80px;text-align:center}
.tl .year{font-family:"Ubuntu",sans-serif;font-size:10px;color:var(--gray)}
.tl h4{font-weight:400;font-size:7.5px;color:var(--gray);line-height:1.2;margin:52px 0 8px}
.tl p{font-size:5px}

.donut-label{position:absolute;top:212px;width:150px;text-align:center}
.donut-label h4{font-weight:600;font-size:8px;color:var(--green-dark);margin-bottom:5px}
.donut-label p{font-size:5px}

.chart-note{position:absolute;top:209px;width:210px}
.chart-note h4{font-weight:600;font-size:8px;color:var(--green-dark);margin-bottom:4px}
.chart-note p{font-size:5px}

.stat{position:absolute;width:130px;text-align:center}
.stat strong{display:block;font-family:"Ubuntu",sans-serif;font-weight:400;font-size:20px;color:var(--green-dark);margin-bottom:3px}
.stat strong.light{color:var(--green-light)}
.stat p{font-size:5px}

table.data{position:absolute;left:20px;top:86px;width:492px;border-collapse:collapse;font-size:5.8px}
table.data th{background:var(--green-light);color:var(--green-dark);font-weight:600;padding:3px 4px;font-size:6px;line-height:1.2}
table.data th:nth-child(2){background:var(--green-dark);color:#fff}
table.data th.empty{background:none}
table.data td{border-bottom:1px solid var(--gray-light);height:22.5px;text-align:center}
table.data td:first-child{text-align:left;padding-left:4px;width:170px}
table.data td.hi{color:var(--green)}

.section-title{position:absolute;left:45px;top:120px;font-family:"Ubuntu",sans-serif;font-weight:400;font-size:30px;color:var(--green-dark)}
.section-text{position:absolute;left:45px;top:162px;width:210px;font-size:6.5px;color:var(--gray)}

.contact{position:absolute;left:45px;top:140px;color:var(--gray);font-size:6px}
.contact h4{font-weight:600;font-size:9px;color:var(--green-dark);margin-bottom:8px}
.contact address{font-style:normal;margin-bottom:12px}
.contact li{list-style:none;display:flex;align-items:center;gap:7px;margin-bottom:5px}
.contact svg{width:9px;height:9px}
</style>
</head>
<body>

<section class="stage">
  <div class="stage-logo">Kalmora<small>CONSULTING</small></div>
  <div class="slide stage-slide">
    <div class="photo-bg" role="img" aria-label="Soft-focus photo of fresh green tea leaves"></div>
    <div class="cover-logo">Kalmora<small>CONSULTING</small></div>
    <h1 class="cover-title">Presentation<br>Title Goes Here!</h1>
    <p class="cover-sub">Subtitle of Presentation Goes Here</p>
    <span class="url-pill">www.kalmora-consulting.example</span>
    <p class="cover-copy">Copyright © Kalmora Consulting GmbH. All Rights Reserved</p>
  </div>
</section>

<!-- Row 1 -->
<article class="slide" style="left:28px;top:763px">
  <div class="photo-bg" role="img" aria-label="Soft-focus photo of fresh green tea leaves"></div>
  <div class="cover-logo">Kalmora<small>CONSULTING</small></div>
  <h1 class="cover-title">Presentation<br>Title Goes Here!</h1>
  <p class="cover-sub">Subtitle of Presentation Goes Here</p>
  <span class="url-pill">www.kalmora-consulting.example</span>
  <p class="cover-copy">Copyright © Kalmora Consulting GmbH. All Rights Reserved</p>
</article>

<article class="slide" style="left:609px;top:763px">
  <div class="title-tab"></div>
  <h2 class="slide-title">Slide <b>Title</b> Goes Here</h2>
  <div class="body-text">
    <p>Lorem ipsum dolor sit amet, consectetur adipiscing elit. Vivamus eu dui ex. Curabitur dapibus dignissim dui, in molestie metus feugiat sed. Praesent aliquet lorem ex, eu dapibus odio varius at. Duis eget tellus porta, consequat lacus vitae, venenatis dolor. Nulla facilisi. In et sollicitudin lacus. Donec risus orci, gravida sit amet risus vehicula, aliquet pretium sapien. Nullam sit amet magna non ex bibendum mollis. Nunc vel neque eu augue dignissim congue ut vitae magna. Phasellus eget commodo arcu. Nunc vitae semper dui. Integer venenatis, tellus sit amet interdum pretium, erat neque rhoncus turpis, a aliquam augue ligula eget erat. Nunc placerat, arcu nec mattis fermentum, nisi mauris convallis nunc, ut luctus nunc nisl id ex. Nam semper tristique mauris, et vestibulum leo fringilla vel.</p>
    <p>Curabitur dapibus dignissim dui, in molestie metus feugiat sed. Praesent aliquet lorem ex, eu dapibus odio varius at. Duis eget tellus porta, consequat lacus vitae, venenatis dolor. Nulla facilisi. In et sollicitudin lacus. Donec risus orci, gravida sit amet risus vehicula, aliquet pretium sapien. Nullam sit amet magna non ex bibendum mollis. Nunc vel neque eu augue dignissim congue ut vitae magna. Phasellus eget commodo arcu. Nunc vitae semper dui. Integer venenatis, tellus sit amet interdum pretium, erat neque rhoncus turpis, a aliquam augue ligula eget erat. Nunc placerat, arcu nec mattis fermentum, nisi mauris convallis nunc, ut luctus nunc nisl id ex. Nam semper tristique mauris, et vestibulum leo fringilla vel. Nulla id augue eleifend, egestas ligula et, consequat massa. Pellentesque habitant morbi tristique senectus et netus et malesuada fames ac turpis egestas.</p>
  </div>
  <span class="foot-logo">Kalmora<small>CONSULTING</small></span>
  <div class="foot-bar"><span>Copyright © Kalmora Consulting GmbH. All Rights Reserved</span><i>2</i></div>
</article>

<!-- Row 2 -->
<article class="slide" style="left:28px;top:1098px">
  <div class="team-band"></div>
  <h2 class="slide-title">Management <b>Team</b></h2>
  <div class="member" style="left:48px"><span class="portrait" role="img" aria-label="Portrait photo of team member"></span><h3>Dr. Lena Albrecht</h3><p class="role">Managing Partner</p><p>Lorem ipsum dolor sit amet, consectetur adipiscing elit. Vivamus eu dui ex. Curabitur dapibus dignissim dui, in molestie metus feugiat sed.</p></div>
  <div class="member" style="left:211px"><span class="portrait" role="img" aria-label="Portrait photo of team member"></span><h3>Dr. Mira Stein</h3><p class="role">Managing Partner</p><p>Lorem ipsum dolor sit amet, consectetur adipiscing elit. Vivamus eu dui ex. Curabitur dapibus dignissim dui, in molestie metus feugiat sed.</p></div>
  <div class="member" style="left:374px"><span class="portrait" role="img" aria-label="Portrait photo of team member"></span><h3>Dr. Carla Westhoff-Brandt</h3><p class="role">Managing Partner</p><p>Lorem ipsum dolor sit amet, consectetur adipiscing elit. Vivamus eu dui ex. Curabitur dapibus dignissim dui, in molestie metus feugiat sed.</p></div>
  <span class="foot-logo">Kalmora<small>CONSULTING</small></span>
  <div class="foot-bar"><span>Copyright © Kalmora Consulting GmbH. All Rights Reserved</span><i>3</i></div>
</article>

<article class="slide" style="left:609px;top:1098px">
  <div class="title-tab"></div>
  <h2 class="slide-title"><b>Column</b> Slide</h2>
  <div class="col" style="left:41px">
    <h3>Heading Goes Here</h3>
    <ul>
      <li>Lorem ipsum dolor sit amet, consectetur adipiscing elit. Vivamus eu dui ex. Curabitur dapibus dignissim dui, in molestie metus feugiat sed. Praesent aliquet lorem ex, eu dapibus odio varius at. Duis eget tellus porta, consequat lacus vitae, venenatis dolor. Nulla facilisi. In et sollicitudin lacus.</li>
      <li>Donec risus orci, gravida sit amet risus vehicula, aliquet pretium sapien. Nullam sit amet magna non ex bibendum mollis. Nunc vel neque eu augue dignissim congue ut vitae magna. Phasellus eget commodo arcu.</li>
      <li>Nunc vitae semper dui. Integer venenatis, tellus sit amet interdum pretium, erat neque rhoncus turpis, a aliquam augue ligula eget erat. Nunc placerat, arcu nec mattis fermentum, nisi mauris convallis nunc, ut luctus nunc nisl id ex.</li>
    </ul>
  </div>
  <div class="col" style="left:306px">
    <h3>Heading Goes Here</h3>
    <ul>
      <li>Lorem ipsum dolor sit amet, consectetur adipiscing elit. Vivamus eu dui ex. Curabitur dapibus dignissim dui, in molestie metus feugiat sed. Praesent aliquet lorem ex, eu dapibus odio varius at. Duis eget tellus porta, consequat lacus vitae, venenatis dolor. Nulla facilisi. In et sollicitudin lacus.</li>
      <li>Donec risus orci, gravida sit amet risus vehicula, aliquet pretium sapien. Nullam sit amet magna non ex bibendum mollis. Nunc vel neque eu augue dignissim congue ut vitae magna. Phasellus eget commodo arcu.</li>
      <li>Nunc vitae semper dui. Integer venenatis, tellus sit amet interdum pretium, erat neque rhoncus turpis, a aliquam augue ligula eget erat. Nunc placerat, arcu nec mattis fermentum, nisi mauris convallis nunc, ut luctus nunc nisl id ex.</li>
    </ul>
  </div>
  <span class="foot-logo">Kalmora<small>CONSULTING</small></span>
  <div class="foot-bar"><span>Copyright © Kalmora Consulting GmbH. All Rights Reserved</span><i>4</i></div>
</article>

<!-- Row 3 -->
<article class="slide" style="left:28px;top:1433px">
  <div class="title-tab"></div>
  <h2 class="slide-title"><b>Heading Goes Here</b></h2>
  <div class="box" style="left:53px;background:var(--green-dark)"><h3>Lorem ipsum<br>dolor sit amet</h3><p>Lorem ipsum dolor sit amet, consectetur adipiscing elit. Vivamus eu dui ex. Curabitur dapibus dignissim dui, in molestie metus feugiat sed. Praesent aliquet lorem ex, eu dapibus odio varius at. Duis eget tellus porta, consequat lacus vitae, venenatis dolor. Nulla facilisi.</p></div>
  <div class="box" style="left:212px;background:var(--green-light)"><h3>Lorem ipsum<br>dolor sit amet</h3><p>Lorem ipsum dolor sit amet, consectetur adipiscing elit. Vivamus eu dui ex. Curabitur dapibus dignissim dui, in molestie metus feugiat sed. Praesent aliquet lorem ex, eu dapibus odio varius at. Duis eget tellus porta, consequat lacus vitae, venenatis dolor. Nulla facilisi.</p></div>
  <div class="box" style="left:371px;background:var(--gray)"><h3>Lorem ipsum<br>dolor sit amet</h3><p>Lorem ipsum dolor sit amet, consectetur adipiscing elit. Vivamus eu dui ex. Curabitur dapibus dignissim dui, in molestie metus feugiat sed. Praesent aliquet lorem ex, eu dapibus odio varius at. Duis eget tellus porta, consequat lacus vitae, venenatis dolor. Nulla facilisi.</p></div>
  <span class="foot-logo">Kalmora<small>CONSULTING</small></span>
  <div class="foot-bar"><span>Copyright © Kalmora Consulting GmbH. All Rights Reserved</span><i>5</i></div>
</article>

<article class="slide" style="left:609px;top:1433px">
  <div class="title-tab"></div>
  <h2 class="slide-title"><b>Timeline</b> Slide</h2>
  <svg width="562" height="315" style="position:absolute;left:0;top:0" aria-hidden="true">
    <line x1="0" y1="110" x2="550" y2="110" stroke="#bbb" stroke-width="1" stroke-dasharray="3 3"/>
    <g fill="var(--green)"><rect x="72" y="107" width="6" height="6"/><rect x="154" y="107" width="6" height="6" fill="var(--green-light)"/><rect x="236" y="107" width="6" height="6"/><rect x="318" y="107" width="6" height="6" fill="var(--green-light)"/><rect x="400" y="107" width="6" height="6"/><rect x="482" y="107" width="6" height="6" fill="var(--green-light)"/></g>
    <circle cx="75" cy="146" r="17" fill="var(--green-dark)"/><circle cx="75" cy="146" r="13" fill="none" stroke="#fff" stroke-width="1"/>
    <path d="M75 137a6 6 0 0 1 4 10.5v3h-8v-3A6 6 0 0 1 75 137z" fill="#fff"/><rect x="72" y="152" width="6" height="2" fill="#fff"/>
    <circle cx="157" cy="146" r="17" fill="var(--green-light)"/><circle cx="157" cy="146" r="13" fill="none" stroke="#fff" stroke-width="1"/>
    <g fill="#fff"><circle cx="153" cy="142" r="3"/><circle cx="161" cy="142" r="3"/><path d="M147 152a6 5 0 0 1 12 0z"/><path d="M155 152a6 5 0 0 1 12 0z"/></g>
    <circle cx="239" cy="146" r="17" fill="var(--green-dark)"/><circle cx="239" cy="146" r="13" fill="none" stroke="#fff" stroke-width="1"/>
    <circle cx="237" cy="144" r="5" fill="none" stroke="#fff" stroke-width="2"/><line x1="241" y1="148" x2="245" y2="152" stroke="#fff" stroke-width="2.5"/>
    <circle cx="321" cy="146" r="17" fill="var(--green-light)"/><circle cx="321" cy="146" r="13" fill="none" stroke="#fff" stroke-width="1"/>
    <rect x="316" y="138" width="10" height="14" fill="#fff"/><g stroke="var(--green-light)"><line x1="318" y1="142" x2="324" y2="142"/><line x1="318" y1="145" x2="324" y2="145"/><line x1="318" y1="148" x2="324" y2="148"/></g>
    <circle cx="403" cy="146" r="17" fill="var(--green-dark)"/><circle cx="403" cy="146" r="13" fill="none" stroke="#fff" stroke-width="1"/>
    <circle cx="403" cy="146" r="6" fill="none" stroke="#fff" stroke-width="3" stroke-dasharray="2.2 1.3"/><circle cx="403" cy="146" r="2.5" fill="#fff"/>
    <circle cx="485" cy="146" r="17" fill="var(--green-light)"/><circle cx="485" cy="146" r="13" fill="none" stroke="#fff" stroke-width="1"/>
    <g fill="#fff"><rect x="478" y="147" width="3" height="5"/><rect x="483" y="144" width="3" height="8"/><rect x="488" y="140" width="3" height="12"/></g>
  </svg>
  <div class="tl" style="left:35px"><div class="year">2010</div><h4>Heading<br>Goes Here</h4><p>Lorem ipsum dolor sit amet, consectetur adipiscing elit. Vivamus eu dui ex. Curabitur dapibus.</p></div>
  <div class="tl" style="left:117px"><div class="year">2014</div><h4>Heading<br>Goes Here</h4><p>Lorem ipsum dolor sit amet, consectetur adipiscing elit. Vivamus eu dui ex. Curabitur dapibus.</p></div>
  <div class="tl" style="left:199px"><div class="year">2017</div><h4>Heading<br>Goes Here</h4><p>Lorem ipsum dolor sit amet, consectetur adipiscing elit. Vivamus eu dui ex. Curabitur dapibus.</p></div>
  <div class="tl" style="left:281px"><div class="year">2018</div><h4>Heading<br>Goes Here</h4><p>Lorem ipsum dolor sit amet, consectetur adipiscing elit. Vivamus eu dui ex. Curabitur dapibus.</p></div>
  <div class="tl" style="left:363px"><div class="year">2020</div><h4>Heading<br>Goes Here</h4><p>Lorem ipsum dolor sit amet, consectetur adipiscing elit. Vivamus eu dui ex. Curabitur dapibus.</p></div>
  <div class="tl" style="left:445px"><div class="year">2023</div><h4>Heading<br>Goes Here</h4><p>Lorem ipsum dolor sit amet, consectetur adipiscing elit. Vivamus eu dui ex. Curabitur dapibus.</p></div>
  <span class="foot-logo">Kalmora<small>CONSULTING</small></span>
  <div class="foot-bar"><span>Copyright © Kalmora Consulting GmbH. All Rights Reserved</span><i>6</i></div>
</article>

<!-- Row 4 -->
<article class="slide" style="left:28px;top:1768px">
  <div class="photo-bg" role="img" aria-label="Soft-focus photo of fresh green tea leaves"></div>
  <h2 class="section-title">Section Break</h2>
  <p class="section-text">Lorem ipsum dolor sit amet, consectetur adipiscing elit. Vivamus eu dui ex. Curabitur dapibus dignissim dui, in molestie metus feugiat sed. Praesent aliquet lorem ex.</p>
</article>

<article class="slide" style="left:609px;top:1768px">
  <div class="title-tab"></div>
  <h2 class="slide-title"><b>Pie Chart</b> Slide</h2>
  <svg width="562" height="315" style="position:absolute;left:0;top:0" aria-hidden="true">
    <g fill="none" stroke-width="9">
      <circle cx="125" cy="142" r="52" stroke="#e2e2e2"/>
      <circle cx="125" cy="142" r="52" stroke="var(--green-dark)" stroke-dasharray="114.4 326.7" transform="rotate(-90 125 142)"/>
      <circle cx="281" cy="142" r="52" stroke="#e2e2e2"/>
      <circle cx="281" cy="142" r="52" stroke="var(--green-light)" stroke-dasharray="212.4 326.7" transform="rotate(-90 281 142)"/>
      <circle cx="437" cy="142" r="52" stroke="#e2e2e2"/>
      <circle cx="437" cy="142" r="52" stroke="var(--gray)" stroke-dasharray="277.7 326.7" transform="rotate(-90 437 142)"/>
    </g>
    <g font-family="Ubuntu, sans-serif" font-size="19" text-anchor="middle">
      <text x="125" y="149" fill="var(--green-dark)">35<tspan font-size="11">%</tspan></text>
      <text x="281" y="149" fill="var(--green-light)">65<tspan font-size="11">%</tspan></text>
      <text x="437" y="149" fill="var(--gray)">85<tspan font-size="11">%</tspan></text>
    </g>
  </svg>
  <div class="donut-label" style="left:50px"><h4>Heading Goes Here</h4><p>Lorem ipsum dolor sit amet, consectetur adipiscing elit. Vivamus eu dui ex. Curabitur dapibus dignissim dui.</p></div>
  <div class="donut-label" style="left:206px"><h4 style="color:var(--green-light)">Heading Goes Here</h4><p>Lorem ipsum dolor sit amet, consectetur adipiscing elit. Vivamus eu dui ex. Curabitur dapibus dignissim dui.</p></div>
  <div class="donut-label" style="left:362px"><h4 style="color:var(--gray)">Heading Goes Here</h4><p>Lorem ipsum dolor sit amet, consectetur adipiscing elit. Vivamus eu dui ex. Curabitur dapibus dignissim dui.</p></div>
  <span class="foot-logo">Kalmora<small>CONSULTING</small></span>
  <div class="foot-bar"><span>Copyright © Kalmora Consulting GmbH. All Rights Reserved</span><i>8</i></div>
</article>

<!-- Row 5 -->
<article class="slide" style="left:28px;top:2103px">
  <div class="title-tab"></div>
  <h2 class="slide-title"><b>Column Chart</b> Slide</h2>
  <svg width="562" height="315" style="position:absolute;left:0;top:0" aria-hidden="true">
    <g font-size="5" fill="#777" text-anchor="end">
      <text x="70" y="102">Category 4</text><text x="70" y="125">Category 3</text><text x="70" y="148">Category 2</text><text x="70" y="171">Category 1</text>
      <text x="320" y="102">Category 4</text><text x="320" y="125">Category 3</text><text x="320" y="148">Category 2</text><text x="320" y="171">Category 1</text>
    </g>
    <g stroke="#ccc" stroke-width=".6"><line x1="78" y1="90" x2="78" y2="178"/><line x1="328" y1="90" x2="328" y2="178"/></g>
    <rect x="78" y="96" width="58" height="8" fill="var(--green-dark)"/><rect x="136" y="96" width="37" height="8" fill="var(--green-light)"/><rect x="173" y="96" width="65" height="8" fill="var(--gray)"/>
    <rect x="78" y="119" width="46" height="8" fill="var(--green-dark)"/><rect x="124" y="119" width="22" height="8" fill="var(--green-light)"/><rect x="146" y="119" width="36" height="8" fill="var(--gray)"/>
    <rect x="78" y="142" width="32" height="8" fill="var(--green-dark)"/><rect x="110" y="142" width="57" height="8" fill="var(--green-light)"/><rect x="167" y="142" width="26" height="8" fill="var(--gray)"/>
    <rect x="78" y="165" width="75" height="8" fill="var(--green-dark)"/><rect x="153" y="165" width="22" height="8" fill="var(--green-light)"/><rect x="175" y="165" width="20" height="8" fill="var(--gray)"/>
    <rect x="328" y="96" width="40" height="8" fill="var(--green-dark)"/><rect x="368" y="96" width="25" height="8" fill="var(--green-light)"/><rect x="393" y="96" width="45" height="8" fill="var(--gray)"/>
    <rect x="328" y="119" width="55" height="8" fill="var(--green-dark)"/><rect x="383" y="119" width="85" height="8" fill="var(--green-light)"/><rect x="468" y="119" width="32" height="8" fill="var(--gray)"/>
    <rect x="328" y="142" width="65" height="8" fill="var(--green-dark)"/><rect x="393" y="142" width="50" height="8" fill="var(--green-light)"/><rect x="443" y="142" width="20" height="8" fill="var(--gray)"/>
    <rect x="328" y="165" width="80" height="8" fill="var(--green-dark)"/><rect x="408" y="165" width="50" height="8" fill="var(--green-light)"/><rect x="458" y="165" width="20" height="8" fill="var(--gray)"/>
    <g font-size="5" fill="#777" text-anchor="middle">
      <text x="78" y="188">0</text><text x="104" y="188">2</text><text x="130" y="188">4</text><text x="156" y="188">6</text><text x="182" y="188">8</text><text x="208" y="188">10</text><text x="234" y="188">12</text><text x="260" y="188">14</text>
      <text x="328" y="188">0</text><text x="371" y="188">5</text><text x="414" y="188">10</text><text x="457" y="188">15</text><text x="500" y="188">20</text>
    </g>
  </svg>
  <div class="chart-note" style="left:45px"><h4>Heading Goes Here</h4><p>Nullam sit amet magna non ex bibendum mollis. Nunc vel neque eu augue dignissim congue ut vitae magna. Phasellus eget commodo arcu. Nunc vitae semper dui. Integer venenatis, tellus sit amet interdum.</p></div>
  <div class="chart-note" style="left:295px"><h4>Heading Goes Here</h4><p>Nullam sit amet magna non ex bibendum mollis. Nunc vel neque eu augue dignissim congue ut vitae magna. Phasellus eget commodo arcu. Nunc vitae semper dui. Integer venenatis, tellus sit amet interdum.</p></div>
  <span class="foot-logo">Kalmora<small>CONSULTING</small></span>
  <div class="foot-bar"><span>Copyright © Kalmora Consulting GmbH. All Rights Reserved</span><i>9</i></div>
</article>

<article class="slide" style="left:609px;top:2103px">
  <div class="title-tab"></div>
  <h2 class="slide-title"><b>Pie Chart</b> Slide</h2>
  <svg width="562" height="315" style="position:absolute;left:0;top:0" aria-hidden="true">
    <g transform="translate(282 150) scale(1 .55)">
      <path d="M-92 0 V34 A92 92 0 0 0 92 34 V0 Z" fill="#4d7d1d"/>
      <path d="M0 0 L0 -92 A92 92 0 0 1 89.8 -20 Z" fill="#3a6e12"/>
      <path d="M0 0 L89.8 -20 A92 92 0 0 1 -55.1 73.7 Z" fill="var(--green-light)"/>
      <path d="M0 0 L-55.1 73.7 A92 92 0 0 1 -91.4 10.7 Z" fill="var(--gray)"/>
      <path d="M0 0 L-91.4 10.7 A92 92 0 0 1 0 -92 Z" fill="var(--green)"/>
    </g>
    <g font-size="8" fill="#fff" font-family="Ubuntu, sans-serif">
      <text x="226" y="127">25%</text><text x="313" y="125">20%</text><text x="318" y="166">36%</text><text x="196" y="157">12%</text>
    </g>
  </svg>
  <div class="stat" style="left:38px;top:88px"><strong>25%</strong><p>Nunc placerat, arcu nec mattis fermentum, nisi mauris convallis nunc, ut luctus nunc nisl id ex. Nam semper tristique mauris.</p></div>
  <div class="stat" style="left:38px;top:170px"><strong>12%</strong><p>Nunc placerat, arcu nec mattis fermentum, nisi mauris convallis nunc, ut luctus nunc nisl id ex. Nam semper tristique mauris.</p></div>
  <div class="stat" style="left:397px;top:88px"><strong>20%</strong><p>Nunc placerat, arcu nec mattis fermentum, nisi mauris convallis nunc, ut luctus nunc nisl id ex. Nam semper tristique mauris.</p></div>
  <div class="stat" style="left:397px;top:170px"><strong class="light">36%</strong><p>Nunc placerat, arcu nec mattis fermentum, nisi mauris convallis nunc, ut luctus nunc nisl id ex. Nam semper tristique mauris.</p></div>
  <span class="foot-logo">Kalmora<small>CONSULTING</small></span>
  <div class="foot-bar"><span>Copyright © Kalmora Consulting GmbH. All Rights Reserved</span><i>10</i></div>
</article>

<!-- Row 6 -->
<article class="slide" style="left:28px;top:2438px">
  <div class="title-tab"></div>
  <h2 class="slide-title"><b>Table/Data</b> Slide</h2>
  <table class="data">
    <thead><tr><th class="empty"></th><th>Lorem ipsum<br>amet, consectetur</th><th>Lorem ipsum<br>amet, consectetur</th><th>Lorem ipsum<br>amet, consectetur</th><th>Lorem ipsum<br>amet, consectetur</th></tr></thead>
    <tbody>
      <tr><td>Lorem ipsum dolor sit amet</td><td class="hi">Text Goes Here</td><td>Text Goes Here</td><td>Text Goes Here</td><td>Text Goes Here</td></tr>
      <tr><td>Pellentesque habitant morbi tristique</td><td class="hi">Text Goes Here</td><td>Text Goes Here</td><td>Text Goes Here</td><td>Text Goes Here</td></tr>
      <tr><td>Nullam sit amet magna non ex</td><td class="hi">Text Goes Here</td><td>Text Goes Here</td><td>Text Goes Here</td><td>Text Goes Here</td></tr>
      <tr><td>Vivamus eu dui ex</td><td class="hi">Text Goes Here</td><td>Text Goes Here</td><td>Text Goes Here</td><td>Text Goes Here</td></tr>
      <tr><td>Donec risus orci, gravida sit amet</td><td class="hi">Text Goes Here</td><td>Text Goes Here</td><td>Text Goes Here</td><td>Text Goes Here</td></tr>
      <tr><td>Nulla facilisi. In et sollicitudin lacus</td><td class="hi">Text Goes Here</td><td>Text Goes Here</td><td>Text Goes Here</td><td>Text Goes Here</td></tr>
      <tr><td>Nunc vel neque eu augue dignissim</td><td class="hi">Text Goes Here</td><td>Text Goes Here</td><td>Text Goes Here</td><td>Text Goes Here</td></tr>
    </tbody>
  </table>
  <span class="foot-logo">Kalmora<small>CONSULTING</small></span>
  <div class="foot-bar"><span>Copyright © Kalmora Consulting GmbH. All Rights Reserved</span><i>11</i></div>
</article>

<article class="slide" style="left:609px;top:2438px">
  <div class="photo-bg" role="img" aria-label="Soft-focus photo of fresh green tea leaves"></div>
  <div class="cover-logo" style="top:82px">Kalmora<small>CONSULTING</small></div>
  <div class="contact">
    <h4>Contact Us</h4>
    <address>Nachhaltigkeitsberatung<br>Lindenhof Business Park<br>Am Gartenweg 12<br>61000 Musterstadt / Frankfurt a. M.</address>
    <ul>
      <li><svg viewBox="0 0 10 10"><path d="M2 1l2 2-1 1.5a5 5 0 0 0 2.5 2.5L7 6l2 2-1.5 1.5C4 9 1 6 .5 2.5z" fill="var(--green-dark)"/></svg>+49 (0) 6100 – 555 0123</li>
      <li><svg viewBox="0 0 10 10"><circle cx="5" cy="5" r="2" fill="none" stroke="var(--green-dark)" stroke-width="1.2"/><path d="M7 3v3a1.3 1.3 0 0 0 2.3 0A4.5 4.5 0 1 0 7.5 9" fill="none" stroke="var(--green-dark)" stroke-width="1.2"/></svg>info@kalmora-consulting.example</li>
      <li><svg viewBox="0 0 10 10"><circle cx="5" cy="5" r="4.2" fill="none" stroke="var(--green-dark)"/><ellipse cx="5" cy="5" rx="1.8" ry="4.2" fill="none" stroke="var(--green-dark)" stroke-width=".8"/><line x1=".8" y1="5" x2="9.2" y2="5" stroke="var(--green-dark)" stroke-width=".8"/></svg>www.kalmora-consulting.example</li>
    </ul>
  </div>
  <p class="cover-copy">Copyright © Kalmora Consulting GmbH. All Rights Reserved</p>
</article>

</body>
</html>
```